Packaging design for aloe lotion bottle for a Laser Clinic

We need a packaging design for a body lotion bottle. Our business is a laser clinic and we are looking at slowly rolling out a range of skincare products. This lotion bottle is the first item with more to follow so the winning designer will have other designs to work on in the future.

The design needs to be classy, elegant, strong and sophisticated. The bottle will be clear with a shiny silver sleeved lid. The lotion itself, which will be visible through the bottle, will be a very light green colour. Think Mirelle Davonne and Voriel as that is the image I want to convey.

Ideally we were thinking of having a design with a single colour but if you come up with a fantastic multi colour design that we love then we're open to it.

Reason: I have extended the deadline as I feel I need more time to allow designers to submit their designs. I haven't found a design that I love just yet. The project has been made a guaranteed payment upon completion. Thank you.

Target Market(s)

upper class high income earners with a high disposable income. People that look after themselves

Industry/Entity Type

Beauty Salon

Colors
000000
cadf82

Requirements
Must have
• must include the details below:
• Post Laser Calming Cream
• This soothing and calming anti inflammatory cream is specifically formulated for use after post laser treatments.
• Fresh Cucumber, Melon and Aloe Vera Leaf Juice blend together in perfect harmony to quickly cool you skin and restore your skins natural moisture.
• Our luxurious calming cream targets redness and helps to reduce inflammation, bringing you supple and radiant skin like never before.
• Directions: Use a liberal amount twice daily on all your treatment areas. This nourishing cream can also be used daily to restore moisture and softness to areas of the face and body not being treated by laser or IPL.
• Ingredients: water (aqua), glycine soja (soybean) oil, cetyl alcohol, glycerin dimethicone, butyrospermum parkii (shea butter), theobroma cacao (cocoa) seed butter, aloe barbadensis (aloe vera) leaf juice, tocopheryl acetate, sodium ascorbyl phosphate, disodium EDTA, ceteareth-20, carbomer, BHT, benzyl benzoate, butylphenyl methylpropional, hexyl cinnamal, linalool, glyceryl caprylate, methylisothiazolinone. May contain: Red 4 (CI 14700, aka 504), Yellow 5 (CI 19140, Ki4), Yellow 6 (CI 15985, KI5), Blue 1 (CI 42090, Ao1), Red 33 (CI 17200, Aka 227), Ext. Violet 2 (CI 60730, Murasaki401), Green 3 (CI 42053, Midori3)
• Against Animal Testing
• Manufactured in Australia
• www.velvetglowclinic.com.au
• 500ml
• Pure Halo Laser Hair Removal logo (see attached files)
Nice to have
• A sophisticated and elegant design
Should not have
• no photos. not too many different colours

```html
<!DOCTYPE html>
<html lang="en">
<head>
<meta charset="utf-8">
<title>Pure Halo – Post Laser Calming Cream Label</title>
<link rel="stylesheet" href="https://fonts.googleapis.com/css2?family=Arimo:wght@400;700&family=Josefin+Sans:wght@400&display=swap">
<style>
  :root {
    --backdrop: #b9b9b9;
    --label: #cadf82;
    --label-shade: #bfd674;
    --ink: #000000;
  }
  html, body {
    margin: 0;
    padding: 0;
    width: 1200px;
    height: 1200px;
    overflow: hidden;
    background: var(--backdrop);
  }
  .canvas {
    position: relative;
    width: 1200px;
    height: 1200px;
    background: var(--backdrop);
  }
  .label {
    position: absolute;
    left: 280px;
    top: 130px;
    width: 640px;
    height: 940px;
    background: linear-gradient(90deg, var(--label-shade) 0%, var(--label) 30%, var(--label) 70%, var(--label-shade) 100%);
    color: var(--ink);
    text-align: center;
  }
  .block {
    position: absolute;
    left: 40px;
    right: 40px;
    margin: 0;
  }
  .description {
    top: 40px;
    font-family: "Arimo", sans-serif;
    font-size: 15px;
    line-height: 1.45;
  }
  .description p { margin: 0 0 10px; }
  .brand { top: 290px; }
  .brand-name {
    font-family: "Josefin Sans", sans-serif;
    font-weight: 400;
    font-size: 78px;
    line-height: 1;
    letter-spacing: -1px;
    margin: 0;
  }
  .brand-tagline {
    font-family: "Josefin Sans", sans-serif;
    font-weight: 400;
    font-size: 27px;
    letter-spacing: 5.5px;
    margin: 10px 0 0;
  }
  .product-name {
    top: 445px;
    font-family: "Arimo", sans-serif;
    font-weight: 400;
    font-size: 34px;
    line-height: 1.4;
  }
  .directions {
    top: 560px;
    font-family: "Arimo", sans-serif;
    font-size: 13px;
    line-height: 1.45;
  }
  .ingredients {
    top: 660px;
    font-family: "Arimo", sans-serif;
    font-size: 10.5px;
    line-height: 1.4;
  }
  .label-heading { font-weight: 700; }
  .footer-details {
    top: 845px;
    font-family: "Arimo", sans-serif;
    font-size: 12px;
    letter-spacing: 1px;
  }
  .volume {
    top: 875px;
    font-family: "Arimo", sans-serif;
    font-weight: 400;
    font-size: 27px;
  }
</style>
</head>
<body>
  <main class="canvas">
    <section class="label">
      <div class="block description">
        <p>This soothing and calming anti inflammatory cream is specifically formulated for use after post laser treatments.</p>
        <p>Fresh Cucumber, Melon and Aloe Vera Leaf Juice blend together in perfect harmony to quickly cool your skin and restore your skin's natural moisture.</p>
        <p>Our luxurious calming cream targets redness and helps to reduce inflammation, bringing you supple and radiant skin like never before.</p>
      </div>

      <div class="block brand">
        <p class="brand-name">PURE HALO</p>
        <p class="brand-tagline">LASER HAIR REMOVAL</p>
      </div>

      <h1 class="block product-name">POST LASER CALMING<br>CREAM</h1>

      <p class="block directions"><span class="label-heading">Directions:</span> Use a liberal amount twice daily on all your treatment areas. This nourishing cream can also be used daily to restore moisture and softness to areas of the face and body not being treated by laser or IPL.</p>

      <p class="block ingredients"><span class="label-heading">Ingredients:</span> water (aqua), glycine soja (soybean) oil, cetyl alcohol, glycerin dimethicone, butyrospermum parkii (shea butter), theobroma cacao (cocoa) seed butter, aloe barbadensis (aloe vera) leaf juice, tocopheryl acetate, sodium ascorbyl phosphate, disodium EDTA, ceteareth-20, carbomer, BHT, benzyl benzoate, butylphenyl methylpropional, hexyl cinnamal, linalool, glyceryl caprylate, methylisothiazolinone. May contain: Red 4 (CI 14700, aka 504), Yellow 5 (CI 19140, Ki4), Yellow 6 (CI 15985, KI5), Blue 1 (CI 42090, Ao1), Red 33 (CI 17200, Aka 227), Ext. Violet 2 (CI 60730, Murasaki401), Green 3 (CI 42053, Midori3)</p>

      <p class="block footer-details">AGAINST ANIMAL TESTING · MANUFACTURED IN AUSTRALIA · www.velvetglowclinic.com.au</p>

      <p class="block volume">500ML</p>
    </section>
  </main>
</body>
</html>
```